Criminal Defense Lawyer needs Website
Venturo Law Office
Criminal Defense Lawyer needs Website - Law
Creative Brief
Law
venturolawoffice.com
Ned Venturo of Venturo Law Office is dedicated exclusively to the practice of criminal law. Areas of Practice: DUI Felony Charges Misdemeanor Charges Criminal Record Expungements Driver's License Reinstatement Traffic Tickets
below header
http://telbrolaw.com
http://wdmlaw.com
http://www.pelvanostrick.com
I am looking for a cutting edge design. welcome screen should be more visual than informative. It should be a portal to each individual sub-page. please refer to my current website, venturolawoffice.com, for content related information. I would like the same secondary pages as my current site: attorney profile, legal services, duo, etc... I would like a website that is simple yet cutting edge on the welcome screen. It needs to incorporate my logo and one of the full or three quarter body portraits i have included. do not include the close up or casual photo on the welcome screen; those are reserved for the attorney profile page. feel free to use a background fill on the portraits if necessary. please be creative on menu navigation. CREATIVE MENU DESIGN ON THE WELCOME SCREEN IS A MUST!
moomtaz moomtaz
Designers, Thank you for your designs. I will pick a winner in the next few days after consulting my staff.
I understand that other concepts are veiled. The following websites have what I consider creative and dynamic menu design: http://www.q-vlaw.com http://dornaklawllc.com http://farquist-firm.com
Designers, Please submit some welcome page designs incorporating photo entitled 2015_Ned_Venturo_Business_Portraits_8_51884.jpg Would like to see full body length and 3/4 length versions. Thank you.
I like the unconventional menu design in #20 and #22. That is the type of creative menu I discussed in my brief.
Just to let designers know, during the first few days of the contest I will be giving three stars to designs that appeal to mE. This will let all designers know where to concentrate the designs. Closer to the end of the contest I will upgrade the finalists to four and five stars. I will give feedback to certain designs throughout the contest if I need specific changes. Please refer to my brief for a general approach. Some have done this, others have not.

```html
<!DOCTYPE html>
<html lang="en">
<head>
<meta charset="utf-8">
<title>Venturo Law Office – Welcome Screen Concepts</title>
<link href="https://fonts.googleapis.com/css2?family=Oswald:wght@400;500&family=Lato:wght@400;700&display=swap" rel="stylesheet">
<style>
:root{
  --stage-light:#d9d9d9;
  --stage-dark:#9a9a9a;
  --page:#0b0b0b;
  --panel-edge:#000;
  --ink:#f2f2f2;
  --muted:#8c8c8c;
  --accent:#b3267a;
  --button:#1b1b1b;
  --button-edge:#3a3a3a;
  --date:#c9c9c9;
}
*{margin:0;padding:0;box-sizing:border-box}
html,body{width:1200px;height:857px;overflow:hidden}
body{
  background:radial-gradient(ellipse at center,var(--stage-light) 0%,var(--stage-dark) 100%);
  font-family:"Lato",Arial,sans-serif;color:var(--ink);position:relative;
}
.screen{
  position:absolute;width:510px;height:368px;background:var(--page);
  overflow:hidden;box-shadow:0 4px 14px rgba(0,0,0,.45);
}
.screen--welcome{left:72px;top:29px}
.screen--felony{left:619px;top:29px}
.screen--dui{left:72px;top:432px}
.screen--misdemeanor{left:619px;top:432px}

.backdrop{position:absolute;inset:0}
.screen--welcome .backdrop{background:radial-gradient(ellipse at 50% 20%,#3a2a1c 0%,#121010 45%,#050505 100%)}
.screen--felony .backdrop{background:radial-gradient(ellipse at 45% 18%,#4a4a4a 0%,#1a1a1a 45%,#060606 100%)}
.screen--dui .backdrop{background:linear-gradient(160deg,#5a5e62 0%,#2a2c2e 30%,#0c0c0c 65%,#060606 100%)}
.screen--misdemeanor .backdrop{background:linear-gradient(200deg,#6a6f74 0%,#2b2f33 35%,#0a0a0a 70%,#050505 100%)}

.site-header{position:absolute;left:0;top:0;width:100%;height:28px}
.brand{position:absolute;left:162px;top:7px;display:flex;align-items:center;gap:4px}
.brand-mark{width:14px;height:14px;border-radius:50%;background:var(--ink)}
.brand-name{font-family:"Oswald",sans-serif;font-size:9px;letter-spacing:1px;color:var(--ink)}
.contact{position:absolute;left:330px;top:6px;font-size:5px;line-height:7px;color:var(--muted);text-align:right}

.hero{position:absolute;left:120px;top:30px;width:270px;height:76px}
.hero-photo{position:absolute;top:0;height:100%}
.hero-copy{position:absolute;top:14px;font-family:"Oswald",sans-serif;color:var(--ink);line-height:1.05}
.hero-title{font-size:12px;text-transform:uppercase}
.hero-sub{font-size:5px;color:var(--muted);margin-top:2px;letter-spacing:.5px}
.hero-rule{width:70px;height:1px;background:var(--accent);margin:4px 0}
.hero-button{display:inline-block;font-size:4.5px;background:var(--button);border:1px solid var(--button-edge);padding:2px 5px;margin-top:4px;font-family:"Lato",sans-serif}

.screen--welcome .hero-photo{left:0;width:270px;background:linear-gradient(90deg,#2a2420 0%,#50473e 25%,#2e2b29 45%,#151515 70%,#0d0d0d 100%)}
.screen--welcome .hero-copy{left:140px}
.screen--felony .hero-photo{left:0;width:270px;background:linear-gradient(90deg,#1a1a1a 0%,#5a5550 30%,#8d7f72 50%,#3a3a3a 75%,#181818 100%)}
.screen--felony .hero-copy{left:130px;top:30px}
.screen--dui .hero-photo{left:0;width:270px;background:linear-gradient(90deg,#2a1a0c 0%,#8a5a22 25%,#3f3a36 50%,#2a2a2a 80%,#1a1a1a 100%)}
.screen--dui .hero-copy{left:130px;top:26px}
.screen--misdemeanor .hero-photo{left:0;width:270px;background:linear-gradient(90deg,#2a2c30 0%,#5e6a7c 25%,#8f7b6a 45%,#33363a 75%,#1a1a1a 100%)}
.screen--misdemeanor .hero-copy{left:130px;top:30px}

.practice{position:absolute;left:150px;top:112px;width:220px;text-align:center}
.practice-title{font-family:"Oswald",sans-serif;font-size:7px;letter-spacing:1px;line-height:8px}
.practice-title small{display:block;font-size:4.5px;color:var(--muted)}
.practice-grid{display:grid;grid-template-columns:repeat(3,1fr);gap:5px 6px;margin-top:5px}
.practice-item{height:17px;background:var(--button);border:1px solid var(--button-edge);font-family:"Oswald",sans-serif;font-size:4.6px;display:flex;align-items:center;justify-content:center;padding:0 3px;line-height:1.1}

.news{position:absolute;left:150px;top:182px;width:220px;display:flex;gap:10px}
.news-col{flex:1}
.news-title{font-family:"Oswald",sans-serif;font-size:5.5px;border-bottom:1px solid var(--accent);padding-bottom:2px;margin-bottom:4px}
.intro{display:flex;gap:4px}
.intro-photo{width:34px;height:26px;flex:none;background:linear-gradient(135deg,#4a3a2a,#1e1a16)}
.intro-text{font-size:4px;line-height:5.5px;color:var(--muted)}
.post{display:flex;gap:4px;align-items:center;margin-bottom:3px}
.post-date{font-family:"Oswald",sans-serif;font-size:7px;color:var(--date);width:12px;line-height:6px;text-align:center}
.post-date small{display:block;font-size:3.5px;color:var(--muted)}
.post-text{font-size:4.2px;color:var(--ink)}

.site-footer{position:absolute;left:150px;top:244px;width:220px;display:flex;justify-content:space-between;align-items:center}
.social{display:flex;gap:3px}
.social span{width:7px;height:7px;background:#4a4a4a;display:block}
.pay{font-size:4px;background:var(--accent);padding:2px 4px}
</style>
</head>
<body>

<section class="screen screen--welcome">
  <div class="backdrop" role="img" aria-label="Dark courtroom interior with a judge's gavel"></div>
  <header class="site-header">
    <div class="brand"><span class="brand-mark"></span><span class="brand-name">VENTURO</span></div>
    <div class="contact">24/7 FREE CONSULTATION<br>(555) 014-2290</div>
  </header>
  <div class="hero">
    <div class="hero-photo" role="img" aria-label="Portrait of attorney Ned Venturo in a dark suit"></div>
    <div class="hero-copy">
      <div class="hero-title">Welcome to<br>Venturo Law Office</div>
      <div class="hero-sub">NED VENTURO, ATTORNEY AT LAW</div>
      <div class="hero-button">LEARN MORE</div>
    </div>
  </div>
  <div class="practice">
    <div class="practice-title">CRIMINAL DEFENSE<small>AREAS OF PRACTICE</small></div>
    <div class="practice-grid">
      <div class="practice-item">DUI</div><div class="practice-item">FELONY CHARGES</div><div class="practice-item">MISDEMEANOR CHARGES</div>
      <div class="practice-item">CRIMINAL RECORD EXPUNGEMENTS</div><div class="practice-item">DRIVER'S LICENSE REINSTATEMENT</div><div class="practice-item">TRAFFIC TICKETS</div>
    </div>
  </div>
  <div class="news">
    <div class="news-col"><div class="news-title">WELCOME TO VENTURO</div>
      <div class="intro"><div class="intro-photo" role="img" aria-label="Attorney at his desk"></div><p class="intro-text">Focused solely on criminal defense for clients across the county.</p></div></div>
    <div class="news-col"><div class="news-title">LATEST BLOG POSTS</div>
      <div class="post"><div class="post-date">12<small>JAN</small></div><div class="post-text">New DUI limits explained</div></div>
      <div class="post"><div class="post-date">03<small>FEB</small></div><div class="post-text">Sealing an old record</div></div>
      <div class="post"><div class="post-date">21<small>MAR</small></div><div class="post-text">Getting your license back</div></div></div>
  </div>
  <footer class="site-footer"><div class="social"><span></span><span></span><span></span><span></span></div><div class="pay">Pay online</div></footer>
</section>

<section class="screen screen--felony">
  <div class="backdrop" role="img" aria-label="Dim prison corridor with steel bars"></div>
  <header class="site-header">
    <div class="brand"><span class="brand-mark"></span><span class="brand-name">VENTURO</span></div>
    <div class="contact">24/7 FREE CONSULTATION<br>(555) 014-2290</div>
  </header>
  <div class="hero">
    <div class="hero-photo" role="img" aria-label="Hands holding jail cell bars"></div>
    <div class="hero-copy"><div class="hero-title">Felony Charges</div><div class="hero-rule"></div><div class="hero-button">LEARN MORE</div></div>
  </div>
  <div class="practice">
    <div class="practice-title">CRIMINAL DEFENSE<small>AREAS OF PRACTICE</small></div>
    <div class="practice-grid">
      <div class="practice-item">DUI</div><div class="practice-item">FELONY CHARGES</div><div class="practice-item">MISDEMEANOR CHARGES</div>
      <div class="practice-item">CRIMINAL RECORD EXPUNGEMENTS</div><div class="practice-item">DRIVER'S LICENSE REINSTATEMENT</div><div class="practice-item">TRAFFIC TICKETS</div>
    </div>
  </div>
  <div class="news">
    <div class="news-col"><div class="news-title">WELCOME TO VENTURO</div>
      <div class="intro"><div class="intro-photo" role="img" aria-label="Attorney at his desk"></div><p class="intro-text">Focused solely on criminal defense for clients across the county.</p></div></div>
    <div class="news-col"><div class="news-title">LATEST BLOG POSTS</div>
      <div class="post"><div class="post-date">12<small>JAN</small></div><div class="post-text">New DUI limits explained</div></div>
      <div class="post"><div class="post-date">03<small>FEB</small></div><div class="post-text">Sealing an old record</div></div>
      <div class="post"><div class="post-date">21<small>MAR</small></div><div class="post-text">Getting your license back</div></div></div>
  </div>
  <footer class="site-footer"><div class="social"><span></span><span></span><span></span><span></span></div><div class="pay">Pay online</div></footer>
</section>

<section class="screen screen--dui">
  <div class="backdrop" role="img" aria-label="Car parked on a dark street at night"></div>
  <header class="site-header">
    <div class="brand"><span class="brand-mark"></span><span class="brand-name">VENTURO</span></div>
    <div class="contact">24/7 FREE CONSULTATION<br>(555) 014-2290</div>
  </header>
  <div class="hero">
    <div class="hero-photo" role="img" aria-label="Glass of whiskey beside car keys"></div>
    <div class="hero-copy"><div class="hero-title">Driving Under<br>the Influence</div><div class="hero-rule"></div><div class="hero-button">LEARN MORE</div></div>
  </div>
  <div class="practice">
    <div class="practice-title">CRIMINAL DEFENSE<small>AREAS OF PRACTICE</small></div>
    <div class="practice-grid">
      <div class="practice-item">DUI</div><div class="practice-item">FELONY CHARGES</div><div class="practice-item">MISDEMEANOR CHARGES</div>
      <div class="practice-item">CRIMINAL RECORD EXPUNGEMENTS</div><div class="practice-item">DRIVER'S LICENSE REINSTATEMENT</div><div class="practice-item">TRAFFIC TICKETS</div>
    </div>
  </div>
  <div class="news">
    <div class="news-col"><div class="news-title">WELCOME TO VENTURO</div>
      <div class="intro"><div class="intro-photo" role="img" aria-label="Attorney at his desk"></div><p class="intro-text">Focused solely on criminal defense for clients across the county.</p></div></div>
    <div class="news-col"><div class="news-title">LATEST BLOG POSTS</div>
      <div class="post"><div class="post-date">12<small>JAN</small></div><div class="post-text">New DUI limits explained</div></div>
      <div class="post"><div class="post-date">03<small>FEB</small></div><div class="post-text">Sealing an old record</div></div>
      <div class="post"><div class="post-date">21<small>MAR</small></div><div class="post-text">Getting your license back</div></div></div>
  </div>
  <footer class="site-footer"><div class="social"><span></span><span></span><span></span><span></span></div><div class="pay">Pay online</div></footer>
</section>

<section class="screen screen--misdemeanor">
  <div class="backdrop" role="img" aria-label="Hooded figure against a grey concrete wall"></div>
  <header class="site-header">
    <div class="brand"><span class="brand-mark"></span><span class="brand-name">VENTURO</span></div>
    <div class="contact">24/7 FREE CONSULTATION<br>(555) 014-2290</div>
  </header>
  <div class="hero">
    <div class="hero-photo" role="img" aria-label="Handcuffed hands behind a back"></div>
    <div class="hero-copy"><div class="hero-title">Misdemeanor Charges</div><div class="hero-rule"></div><div class="hero-button">LEARN MORE</div></div>
  </div>
  <div class="practice">
    <div class="practice-title">CRIMINAL DEFENSE<small>AREAS OF PRACTICE</small></div>
    <div class="practice-grid">
      <div class="practice-item">DUI</div><div class="practice-item">FELONY CHARGES</div><div class="practice-item">MISDEMEANOR CHARGES</div>
      <div class="practice-item">CRIMINAL RECORD EXPUNGEMENTS</div><div class="practice-item">DRIVER'S LICENSE REINSTATEMENT</div><div class="practice-item">TRAFFIC TICKETS</div>
    </div>
  </div>
  <div class="news">
    <div class="news-col"><div class="news-title">WELCOME TO VENTURO</div>
      <div class="intro"><div class="intro-photo" role="img" aria-label="Attorney at his desk"></div><p class="intro-text">Focused solely on criminal defense for clients across the county.</p></div></div>
    <div class="news-col"><div class="news-title">LATEST BLOG POSTS</div>
      <div class="post"><div class="post-date">12<small>JAN</small></div><div class="post-text">New DUI limits explained</div></div>
      <div class="post"><div class="post-date">03<small>FEB</small></div><div class="post-text">Sealing an old record</div></div>
      <div class="post"><div class="post-date">21<small>MAR</small></div><div class="post-text">Getting your license back</div></div></div>
  </div>
  <footer class="site-footer"><div class="social"><span></span><span></span><span></span><span></span></div><div class="pay">Pay online</div></footer>
</section>

</body>
</html>
```